Design an Elegant Handbag Brand website

I need a webiste design are looking for ideas for a new theme, color scheme, etc. You come up with the general look and feel of the home page and our team will take it from there.
We're only looking for a one (1) page layout which should be fashionable and graphic intensive, but also include the standard homepage links (about us, see our collections, etc)

Target Market(s)

Our customers are fashionable women looking for an animal friendly and environmentally friendly handbag.

Industry/Entity Type

Business

Number of Pages Required

1 page

Font styles to use
Serif
Sans Serif

Requirements
Must have
• Feel free to modify it with different colors or tweaks as you see fit. We are open to all suggestions.
Nice to have

```html
<!DOCTYPE html>
<html lang="en">
<head>
<meta charset="utf-8">
<title>Belle Satchel — Handbags</title>
<link href="https://fonts.googleapis.com/css2?family=Open+Sans:wght@400;600;700&family=Oswald:wght@300;400&family=Playfair+Display:ital,wght@0,400;0,700;1,400;1,700&display=swap" rel="stylesheet">
<style>
:root{
  --ink:#2b2b2b;
  --bar:#333333;
  --footer:#2f2f2f;
  --white:#ffffff;
  --red:#d23a2f;
  --tan:#c9a57f;
  --brown:#9c6a43;
  --navy:#1f3a5c;
  --sky:#cfe6ea;
  --card:#f1f1f1;
  --grey:#666666;
  --line:#e2e2e2;
}
*{margin:0;padding:0;box-sizing:border-box}
html,body{width:1200px;height:2418px;overflow:hidden;background:var(--white)}
body{position:relative;font-family:'Open Sans',sans-serif;color:var(--ink)}
.abs{position:absolute}
.serif{font-family:'Playfair Display',serif}

.top-bar{left:0;top:0;width:1200px;height:48px;background:var(--bar);color:var(--white);font-size:12px;font-weight:600}
.top-bar span{position:absolute;top:16px;display:flex;align-items:center;gap:8px}

.brand{display:flex;align-items:center;gap:10px;font-family:'Open Sans',sans-serif;font-weight:700;font-size:24px;letter-spacing:1px}
.brand i{display:block;width:26px;height:26px;border-radius:50%;background:var(--red)}
.header-brand{left:128px;top:104px;color:var(--red)}
.search{left:386px;top:98px;width:332px;height:44px;border:1px solid #222;font-size:18px;color:#555;padding:10px 20px}
.search svg{position:absolute;right:12px;top:11px}
.nav-top{top:112px;font-size:17px;color:#222}

.hero{left:0;top:194px;width:1200px;height:529px;
  background:
    linear-gradient(180deg,rgba(207,230,234,1) 0,rgba(207,230,234,1) 93px,rgba(207,230,234,0) 93px),
    linear-gradient(180deg,rgba(0,0,0,0) 78%,rgba(110,108,115,.55) 100%),
    linear-gradient(90deg,#ececee 0%,#ebeaec 36%,#e6cfc6 52%,#dcc0b2 62%,#4a4548 74%,#2a2a30 86%,#e9e8ea 96%)}
.hero-title{left:144px;top:212px;font-size:47px;font-weight:700;font-style:italic;color:#111}
.hero-kicker{left:154px;top:364px;font-family:'Oswald',sans-serif;font-weight:300;font-size:26px;color:#222;letter-spacing:1px}
.hero-rule{left:154px;top:416px;width:66px;height:3px;background:#e8c9b0}
.hero-lead{left:154px;top:430px;font-size:32px;font-style:italic;line-height:44px;color:#333}
.hero-note{left:154px;top:540px;font-size:22px;font-style:italic;color:var(--tan)}
.dot{width:16px;height:16px;border-radius:50%;background:var(--white);top:662px}

.promo-left{left:127px;top:764px;width:561px;height:266px;background:linear-gradient(90deg,#7b6b64,#a89f98 55%,#8d7f77)}
.promo-left h3{position:absolute;left:57px;top:50px;font-size:34px;font-style:italic;font-weight:700;line-height:44px;color:var(--white)}
.promo-cta{position:absolute;right:0;bottom:0;width:246px;height:54px;background:var(--brown);color:var(--white);font-family:'Playfair Display',serif;font-weight:700;font-size:16px;text-align:center;line-height:54px}
.promo-right{left:718px;top:764px;width:353px;height:266px;background:linear-gradient(180deg,#4aa8cc 0%,#3a93bd 65%,#1c6f9d 100%)}
.promo-tag{position:absolute;left:211px;top:39px;width:116px;height:37px;background:var(--navy);color:var(--white);font-family:'Playfair Display',serif;font-size:16px;text-align:center;line-height:37px}
.promo-off{position:absolute;left:204px;width:132px;text-align:center;top:92px;font-size:34px;color:var(--white)}
.promo-sub{position:absolute;left:200px;width:140px;top:150px;font-size:26px;font-style:italic;font-weight:700;line-height:29px;color:var(--white);text-align:center}

.section-title{left:0;top:1084px;width:1200px;text-align:center;font-size:26px;font-weight:600;letter-spacing:1px}
.section-rule{left:529px;top:1136px;width:142px;height:3px;background:var(--line)}
.product{top:1164px;width:222px}
.product-photo{width:222px;height:257px}
.product h4{margin-top:18px;font-family:'Playfair Display',serif;font-weight:400;font-size:20px;text-align:center;color:#333}
.product p{margin-top:6px;font-family:'Oswald',sans-serif;font-size:20px;text-align:center;color:#222}
.arrow{top:1287px}
.btn{color:var(--white);font-family:'Playfair Display',serif;font-weight:700;font-size:16px;text-align:center}
.view-all{left:529px;top:1539px;width:142px;height:54px;line-height:54px;background:var(--grey)}

.story-photo{left:0;top:1661px;width:1200px;height:514px;background:linear-gradient(90deg,#8a8070 0%,#a5503a 22%,#8a4533 45%,#8c4a35 70%,#9a8a78 100%)}
.story-card{left:634px;top:1728px;width:438px;height:447px;background:var(--white);text-align:center}
.story-card h2{margin-top:44px;font-size:43px;font-weight:400;color:#222}
.story-card p{margin:22px auto 0;width:345px;font-size:16px;line-height:32px;color:#444}
.story-cta{left:728px;top:2073px;width:247px;height:54px;line-height:54px;background:var(--red)}

.footer{left:0;top:2175px;width:1200px;height:243px;background:var(--footer);color:var(--white)}
.footer-brand{left:128px;top:2238px;color:var(--white);font-size:30px}
.footer-text{left:128px;top:2306px;width:330px;font-size:14px;line-height:21px;color:var(--white)}
.social{top:2231px;width:36px;height:36px;border-radius:50%;background:#7a7a7a}
.footer-nav{right:128px;top:2290px;display:flex;gap:30px;font-family:'Playfair Display',serif;font-weight:700;font-size:16px;color:var(--white)}
.copyright{right:128px;top:2332px;font-size:14px;color:var(--white)}
</style>
</head>
<body>

<div class="abs top-bar">
  <span style="left:128px">WELCOME TO OUR SHOP !</span>
  <span style="left:384px"><svg width="16" height="14" viewBox="0 0 16 14"><path d="M0 1h3l2 8h9l2-6H4" fill="none" stroke="#fff" stroke-width="1.6"/><circle cx="6" cy="12" r="1.4" fill="#fff"/><circle cx="13" cy="12" r="1.4" fill="#fff"/></svg>FREE SHIPPING ON ALL ORDER</span>
  <span style="left:647px"><svg width="20" height="13" viewBox="0 0 20 13"><rect x="1" y="1" width="18" height="11" fill="none" stroke="#fff" stroke-width="1.6"/><circle cx="10" cy="6.5" r="2.5" fill="#fff"/></svg>100% MONEY BACK GUARANTEE</span>
  <span style="left:911px"><svg width="15" height="15" viewBox="0 0 15 15"><circle cx="7.5" cy="7.5" r="6.3" fill="none" stroke="#fff" stroke-width="1.8"/><path d="M7.5 4v4h3" fill="none" stroke="#fff" stroke-width="1.6"/></svg>ONLINE SUPPORT 24/7</span>
</div>

<div class="abs brand header-brand"><i></i>BELLE SATCHEL</div>
<div class="abs search">Search
  <svg width="22" height="22" viewBox="0 0 22 22"><circle cx="9" cy="9" r="6.5" fill="none" stroke="#e0301e" stroke-width="3"/><path d="M14 14l6 6" stroke="#e0301e" stroke-width="3"/></svg>
</div>
<div class="abs nav-top" style="left:778px">New Trendz</div>
<div class="abs nav-top" style="left:905px">Top Selling Collections</div>

<div class="abs hero" role="img" aria-label="Photo of a woman's legs in black heels and a red dress beside a black leather handbag on a white ledge"></div>
<div class="abs serif hero-title">Top Hand Bag Collections</div>
<div class="abs hero-kicker">NEW COLLECTIONS</div>
<div class="abs hero-rule"></div>
<div class="abs serif hero-lead">Specially Made for<br>all women</div>
<div class="abs serif hero-note">90% Pure leather</div>
<div class="abs dot" style="left:157px"></div>
<div class="abs dot" style="left:186px"></div>
<div class="abs dot" style="left:216px"></div>

<div class="abs promo-left" role="img" aria-label="Woman in grey coat carrying a leather handbag on a city street">
  <h3 class="serif">Women's<br>Leather Hand Bag<br>Collection</h3>
  <div class="promo-cta">NOW AVAILABLE - CHECK IT</div>
</div>
<div class="abs promo-right" role="img" aria-label="Round woven rattan bag by the sea">
  <div class="promo-tag">TRENDY BAGS</div>
  <div class="serif promo-off">30% Off</div>
  <div class="serif promo-sub">New Teen<br>Collections</div>
</div>

<div class="abs section-title">TOP COLLECTIONS</div>
<div class="abs section-rule"></div>

<svg class="abs arrow" style="left:52px" width="36" height="36" viewBox="0 0 36 36"><circle cx="18" cy="18" r="16.5" fill="none" stroke="#444" stroke-width="2"/><path d="M21 11l-7 7 7 7" fill="none" stroke="#444" stroke-width="2"/></svg>
<svg class="abs arrow" style="left:1110px" width="36" height="36" viewBox="0 0 36 36"><circle cx="18" cy="18" r="16.5" fill="none" stroke="#444" stroke-width="2"/><path d="M15 11l7 7-7 7" fill="none" stroke="#444" stroke-width="2"/></svg>

<div class="abs product" style="left:128px">
  <div class="product-photo" role="img" aria-label="Black leather tote bag" style="background:radial-gradient(ellipse 45% 42% at 50% 55%,#3a3a3a 0%,#8a8a8a 55%,var(--card) 100%)"></div>
  <h4>Black Leather Bag</h4><p>$ 12.00</p>
</div>
<div class="abs product" style="left:370px">
  <div class="product-photo" role="img" aria-label="Burgundy leather handbag" style="background:radial-gradient(ellipse 45% 38% at 50% 58%,#6a2a36 0%,#a97c84 55%,var(--card) 100%)"></div>
  <h4>Brown Leather Bag</h4><p>$ 21.00</p>
</div>
<div class="abs product" style="left:609px">
  <div class="product-photo" role="img" aria-label="Grey leather tote bag" style="background:radial-gradient(ellipse 45% 40% at 50% 58%,#c4c2bc 0%,#dad9d5 55%,var(--card) 100%)"></div>
  <h4>Grey Leather Bag</h4><p>$ 30.00</p>
</div>
<div class="abs product" style="left:848px">
  <div class="product-photo" role="img" aria-label="Burgundy leather bucket bag with tassel" style="background:radial-gradient(ellipse 45% 40% at 50% 52%,#702534 0%,#ad7b85 55%,var(--card) 100%)"></div>
  <h4>Brown Leather Bag</h4><p>$ 21.00</p>
</div>

<div class="abs btn view-all">VIEW ALL &gt;</div>

<div class="abs story-photo" role="img" aria-label="Woman in a red coat reading on stone steps with a black leather tote"></div>
<div class="abs story-card">
  <h2 class="serif">See Our Collections</h2>
  <p>Gone are the days when shopping online used to be risky. These days, it’s the preferred method to shop anything you can name as it not only ensures you obtain a variety of options to choose from but is atime efficient purchase.</p>
</div>
<div class="abs btn story-cta">VIEW ALL COLLECTIONS &gt;</div>

<div class="abs footer"></div>
<div class="abs brand footer-brand"><i></i>BELLE SATCHEL</div>
<div class="abs footer-text">Vestibulum sagittis, nisl nec pellentesque suscipit, arcu nisi maximus neque, vitae finibus erat odio eu lacus. Curabitur malesuada nec turpis nec.</div>
<div class="abs social" style="left:891px"></div>
<div class="abs social" style="left:939px"></div>
<div class="abs social" style="left:986px"></div>
<div class="abs social" style="left:1034px"></div>
<div class="abs footer-nav"><span>HOME</span><span>ABOUT US</span><span>OUR COLLECTIONS</span><span>CONTACT US</span></div>
<div class="abs copyright">HandBags © 2020 . All Rights Reserved</div>

</body>
</html>
```